Business Executives Need Book Cover Design

We need a custom book cover instead of the boring stock cover that was available on PressLoom.
The current cover can be seen at:
http://www.shelvaro.example/Ledger-Metrics-Leaders-Directors-hoped/dp/7302846615
We like this cover in general (the colors, general layout and picture), but you can see it needs help with the spacing of the Authors names and general design. Also, since it is stock, someone else could have the same cover. It is for business executives so it should be classy. It should communicate that it is for executives. The book is only available in soft cover.

Target Market(s)

Business School students, business executives

Industry/Entity Type

Business

Requirements
Must have
• book name and authors names.

```html
<!DOCTYPE html>
<html lang="en">
<head>
<meta charset="utf-8">
<title>Ledger Metrics for Leaders &amp; Finance Directors 2.0 — Book Cover</title>
<link rel="stylesheet" href="https://fonts.googleapis.com/css2?family=Caladea:wght@700&family=Source+Sans+3:wght@600&display=swap">
<style>
  :root {
    --gold-light: #f6d27a;
    --gold-mid: #c08a2e;
    --gold-deep: #6b4614;
    --gold-edge: #2e1d08;
    --spine: #8c2c3c;
    --spine-dark: #5e1826;
    --spine-light: #a23a4c;
    --stitch: #c98a96;
    --title-ink: #1d2843;
    --title-glow: rgba(255, 240, 200, 0.85);
    --author-ink: #ffffff;
    --placeholder-a: rgba(120, 112, 100, 0.35);
    --placeholder-b: rgba(190, 184, 172, 0.35);
  }
  html, body {
    margin: 0;
    padding: 0;
    width: 828px;
    height: 1200px;
    overflow: hidden;
    background: #ffffff;
  }
  .cover {
    position: relative;
    width: 828px;
    height: 1200px;
    overflow: hidden;
    background:
      radial-gradient(ellipse 620px 700px at 470px 420px,
        var(--gold-light) 0%,
        var(--gold-mid) 38%,
        var(--gold-deep) 72%,
        var(--gold-edge) 100%);
  }
  .leather-surface {
    position: absolute;
    inset: 0 0 0 124px;
  }
  .spine-band {
    position: absolute;
    top: 0;
    left: 0;
    width: 124px;
    height: 1200px;
    background: linear-gradient(90deg, var(--spine-dark) 0%, var(--spine) 30%, var(--spine-light) 70%, var(--spine-dark) 100%);
    box-shadow: 6px 0 14px rgba(0, 0, 0, 0.55);
  }
  .spine-stitch {
    position: absolute;
    top: 0;
    left: 112px;
    width: 0;
    height: 1200px;
    border-left: 2px dashed var(--stitch);
    opacity: 0.7;
  }
  .book-title {
    position: absolute;
    top: 272px;
    left: 124px;
    right: 0;
    margin: 0;
    text-align: center;
    font-family: "Caladea", "Cambria", serif;
    font-weight: 700;
    font-size: 70px;
    line-height: 82px;
    color: var(--title-ink);
    text-shadow:
      0 0 3px var(--title-glow),
      0 0 8px var(--title-glow),
      1px 2px 2px rgba(0, 0, 0, 0.35);
  }
  .book-title span { display: block; }
  .pen-art {
    position: absolute;
    left: 248px;
    top: 540px;
    width: 432px;
    height: 495px;
    background: linear-gradient(225deg, var(--placeholder-b) 0%, var(--placeholder-a) 100%);
  }
  .author-line {
    position: absolute;
    left: 157px;
    top: 1138px;
    margin: 0;
    font-family: "Source Sans 3", "Myriad Pro", sans-serif;
    font-weight: 600;
    font-size: 36px;
    line-height: 40px;
    letter-spacing: 1.2px;
    color: var(--author-ink);
    white-space: nowrap;
  }
</style>
</head>
<body>
  <main class="cover">
    <div class="leather-surface" role="img" aria-label="Warm golden leather texture filling the cover"></div>
    <div class="spine-band"></div>
    <div class="spine-stitch"></div>

    <h1 class="book-title">
      <span>Ledger Metrics for</span>
      <span>Leaders &amp; Finance</span>
      <span>Directors 2.0</span>
    </h1>

    <div class="pen-art" role="img" aria-label="Photo of a silver fountain pen lying diagonally across the cover"></div>

    <p class="author-line">Daniel Voss &amp; Peter R. Calloway</p>
  </main>
</body>
</html>
```